banner ad for a very high end interior designer

Our website only gets a small number of hits per day, but it is often people looking to choose designers to interview. We are going to do a Zolvex remarketing campaign to show ads to people who have previously visited our website. The goal is to make sure they remember the quality and sophistication of our work.
The banner should include pictures of our work. You can see this at www.corinnebalastrodesign.com. Perhaps a single image per banner, or a slideshow within the banner?
The goal is to create awareness and to remind the former website visitor of our work. So it is important to include the logo from our website in the banner ad for visual anchoring and recall. As well, the banner graphics should be of a quality that would be used by Osric Tambel or Pavo Lenk or wexley cousins or vorna or Castelmo.
As for a 'call to action', we can offer "See Our Work in Person" or some simpler wording. If the person clicks on the banner, it will take them to a landing page where they can request free tickets to the Larkmont Residence Interiors Pavilion home. We are designing one of the rooms at that open home event.
Size: either 300 x 250. May buy a second at 320 x 100

```html
<!DOCTYPE html>
<html lang="en">
<head>
<meta charset="utf-8">
<title>Corinne Balastro — Banner Set</title>
<link rel="stylesheet" href="https://fonts.googleapis.com/css2?family=Arimo:wght@400;700&display=swap">
<style>
  :root{
    --page:#ffffff;
    --frame:#9a9a9a;
    --ink:#222222;
    --logo-grey:#5a5a5a;
    --panel-dark:#333333;
    --panel-mid:#5e5e5e;
    --gold:#e8b93a;
    --gold-text:#f3d27a;
    --silver:#d4d4d4;
    --cta-top:#ff8a4a;
    --cta-bottom:#e85a1c;
    --cta-dot:#8a2a0c;
    --room-window:#f6f4f0;
    --room-wall:#e7e2da;
    --room-sofa:#dcd6cd;
    --room-shadow:#b8b0a5;
    --room-floor:#7d776f;
  }
  *{box-sizing:border-box;margin:0;padding:0}
  html,body{width:1200px;height:1200px;overflow:hidden;background:var(--page)}
  body{font-family:"Arimo",Arial,sans-serif;color:var(--ink)}
  .sheet{position:absolute;left:0;top:0;width:850px;height:850px;transform:scale(1.41176);transform-origin:0 0}
  .banner{position:absolute;overflow:hidden;border:1px solid var(--frame);background:var(--page)}
  .banner svg.shapes{position:absolute;left:0;top:0}
  .size-label{position:absolute;font-size:16px;text-align:center;width:120px}
  .logo{position:absolute;text-align:center;font-size:11px;letter-spacing:1.6px;color:var(--logo-grey);white-space:nowrap;line-height:1}
  .headline{position:absolute;color:#fff;font-weight:700;text-align:center;line-height:1.05;
            text-shadow:0 1px 2px rgba(0,0,0,.6)}
  .headline small{font-size:.8em}
  .rule{display:block;height:1px;background:rgba(255,255,255,.6);margin:4px auto}
  .motto{position:absolute;color:var(--gold-text);font-weight:700;text-align:center;line-height:1.1;
         text-shadow:0 1px 2px rgba(0,0,0,.6)}
  .cta{position:absolute;display:flex;align-items:center;justify-content:space-between;
       padding:0 6px 0 7px;background:linear-gradient(var(--cta-top),var(--cta-bottom));
       color:#fff;font-weight:700;font-size:11px;border-radius:2px;box-shadow:0 1px 3px rgba(0,0,0,.4)}
  .cta .play{width:26px;height:26px;border-radius:50%;background:var(--cta-dot);
             border:2px solid #fff3;display:flex;align-items:center;justify-content:center}
</style>
</head>
<body>
<div class="sheet">

  <!-- Leaderboard 728x90 -->
  <div class="banner leaderboard" style="left:69px;top:55px;width:728px;height:90px">
    <svg class="shapes" width="728" height="90" viewBox="0 0 728 90">
      <defs>
        <linearGradient id="roomA" x1="0" y1="0" x2="1" y2="1">
          <stop offset="0" stop-color="var(--room-window)"/>
          <stop offset=".35" stop-color="var(--room-wall)"/>
          <stop offset=".6" stop-color="var(--room-sofa)"/>
          <stop offset=".82" stop-color="var(--room-shadow)"/>
          <stop offset="1" stop-color="var(--room-floor)"/>
        </linearGradient>
        <linearGradient id="darkA" x1="0" y1="0" x2="0" y2="1">
          <stop offset="0" stop-color="var(--panel-mid)"/><stop offset="1" stop-color="var(--panel-dark)"/>
        </linearGradient>
      </defs>
      <rect x="440" y="0" width="288" height="90" fill="url(#roomA)" role="img" aria-label="Photo of a bright living room with white sofa, lamp and glass table"/>
      <path d="M165,0 L462,0 L482,45 L462,90 L165,90 Q150,45 165,0 Z" fill="url(#darkA)"/>
      <path d="M162,0 Q144,45 162,90" fill="none" stroke="var(--gold)" stroke-width="7"/>
      <polyline points="462,0 482,45 462,90" fill="none" stroke="var(--silver)" stroke-width="9"/>
    </svg>
    <div class="logo" style="left:0;top:49px;width:160px">CORINNE BALASTRO</div>
    <div class="headline" style="left:168px;top:4px;width:290px;font-size:21px;line-height:1">
      WE ARE SPECIALIST IN<br>INTERIOR <small>ARCHITECTURE</small>
      <span class="rule" style="width:160px;margin:3px auto"></span>
    </div>
    <div class="motto" style="left:168px;top:54px;width:290px;font-size:15px;line-height:1.05">Your Satisfaction<br>Is Our Motto</div>
    <div class="cta" style="left:585px;top:29px;width:133px;height:35px">SEE OUR WORK
      <span class="play"><svg width="10" height="12" viewBox="0 0 10 12"><path d="M1,0 L10,6 L1,12 Z" fill="#fff"/></svg></span>
    </div>
  </div>
  <div class="size-label" style="left:355px;top:153px">728X90</div>

  <!-- Medium rectangle 300x250 -->
  <div class="banner rectangle" style="left:69px;top:292px;width:300px;height:250px">
    <svg class="shapes" width="300" height="250" viewBox="0 0 300 250">
      <defs>
        <linearGradient id="roomB" x1="0" y1="0" x2="1" y2="1">
          <stop offset="0" stop-color="var(--room-window)"/>
          <stop offset=".35" stop-color="var(--room-wall)"/>
          <stop offset=".6" stop-color="var(--room-sofa)"/>
          <stop offset=".82" stop-color="var(--room-shadow)"/>
          <stop offset="1" stop-color="var(--room-floor)"/>
        </linearGradient>
        <linearGradient id="darkB" x1="0" y1="0" x2="0" y2="1">
          <stop offset="0" stop-color="var(--panel-mid)"/><stop offset="1" stop-color="var(--panel-dark)"/>
        </linearGradient>
      </defs>
      <rect x="140" y="50" width="160" height="200" fill="url(#roomB)" role="img" aria-label="Photo of a bright living room with white sofa and glass table"/>
      <path d="M0,68 Q150,40 300,68 L300,50 L0,50 Z" fill="var(--page)"/>
      <path d="M0,60 L150,60 L166,143 L150,250 L0,250 Z" fill="url(#darkB)"/>
      <polyline points="150,58 168,143 150,252" fill="none" stroke="var(--silver)" stroke-width="8"/>
      <path d="M0,64 Q150,38 300,64" fill="none" stroke="var(--gold)" stroke-width="7"/>
    </svg>
    <div class="logo" style="left:0;top:31px;width:300px">CORINNE BALASTRO</div>
    <div class="headline" style="left:0;top:78px;width:155px;font-size:19px">
      WE ARE<br>SPECIALIST<br>IN<br>INTERIOR<br><small>ARCHITECTURE</small>
      <span class="rule" style="width:120px"></span>
    </div>
    <div class="motto" style="left:0;top:202px;width:155px;font-size:16px">Your Satisfaction<br>Is Our Motto</div>
    <div class="cta" style="left:160px;top:210px;width:133px;height:34px">SEE OUR WORK
      <span class="play"><svg width="10" height="12" viewBox="0 0 10 12"><path d="M1,0 L10,6 L1,12 Z" fill="#fff"/></svg></span>
    </div>
  </div>
  <div class="size-label" style="left:154px;top:551px">300X250</div>

  <!-- Skyscraper 160x600 -->
  <div class="banner skyscraper" style="left:635px;top:208px;width:160px;height:600px">
    <svg class="shapes" width="160" height="600" viewBox="0 0 160 600">
      <defs>
        <linearGradient id="roomC" x1="0" y1="0" x2="0.4" y2="1">
          <stop offset="0" stop-color="var(--room-window)"/>
          <stop offset=".3" stop-color="var(--room-wall)"/>
          <stop offset=".55" stop-color="var(--room-sofa)"/>
          <stop offset=".8" stop-color="var(--room-shadow)"/>
          <stop offset="1" stop-color="var(--room-floor)"/>
        </linearGradient>
        <linearGradient id="darkC" x1="0" y1="0" x2="0" y2="1">
          <stop offset="0" stop-color="var(--panel-mid)"/><stop offset="1" stop-color="var(--panel-dark)"/>
        </linearGradient>
      </defs>
      <rect x="0" y="300" width="160" height="300" fill="url(#roomC)" role="img" aria-label="Photo of a bright living room with white sofa, lamp, window and glass table"/>
      <path d="M0,78 Q80,58 160,78 L160,312 L80,340 L0,312 Z" fill="url(#darkC)"/>
      <polyline points="0,314 80,342 160,314" fill="none" stroke="var(--silver)" stroke-width="8"/>
      <path d="M0,76 Q80,54 160,76" fill="none" stroke="var(--gold)" stroke-width="7"/>
    </svg>
    <div class="logo" style="left:0;top:40px;width:160px;font-size:9px;letter-spacing:1px">CORINNE BALASTRO</div>
    <div class="headline" style="left:0;top:88px;width:160px;font-size:22px;line-height:1.36">
      WE<br>SPECIALIST<br>IN<br>INTERIOR<br><small style="font-size:.78em">ARCHITECTURE</small>
      <span class="rule" style="width:110px"></span>
    </div>
    <div class="motto" style="left:0;top:260px;width:160px;font-size:17px">You Satisfaction<br>Is Our Motto</div>
    <div class="cta" style="left:12px;top:558px;width:136px;height:34px">SEE OUR WORK
      <span class="play"><svg width="10" height="12" viewBox="0 0 10 12"><path d="M1,0 L10,6 L1,12 Z" fill="#fff"/></svg></span>
    </div>
  </div>
  <div class="size-label" style="left:655px;top:816px">160X600</div>

</div>
</body>
</html>
```